New digital business consulting firm needs a professional Wordpress site

Lumora Partners Inc. is a new consulting firm that helps large companies with Digital Transformation. We help companies define a digital transformation strategy for improving the products, processes and customer journey using digital technology.

The website will serve three purposes:
1) Represent what the firm does.
2) Allow people to download research reports.
3) Collect email addresses from people who my be interested in using our services.

The tone of the website should be innovative and professional. The website will have only a few pages. You can see the type of content we wish to post on the current website www.lumorapartners-example.com.

The website will support a book that is about to be released. The book cover is attached. However, the website does not necessarily have to match the book cover. Do not be constrained by the book cover.

Target Market(s)

Executives in large companies

Industry/Entity Type

Management Consulting

Font styles to use
Sans Serif

Requirements
Must have
• Professional and innovative, clean, cool
Nice to have
• None
Should not have
• None

```html
<!DOCTYPE html>
<html lang="en">
<head>
<meta charset="utf-8">
<title>Lumora Partners — Digital Transformation Consulting</title>
<link href="https://fonts.googleapis.com/css2?family=Nunito+Sans:wght@300;400;600;700&display=swap" rel="stylesheet">
<style>
:root{
  --brand-blue:#1d4a86;
  --navy:#17437e;
  --green:#5a8f22;
  --footer-green:#5a9e1a;
  --text:#444;
  --muted:#777;
  --line:#cfd3d8;
  --white:#fff;
}
*{box-sizing:border-box;margin:0;padding:0}
html,body{width:1200px;height:2651px;overflow:hidden}
body{font-family:"Nunito Sans",Arial,sans-serif;color:var(--text);background:var(--white);position:relative}
.abs{position:absolute}

/* header */
.site-header{position:absolute;top:0;left:0;width:1200px;height:90px;background:var(--white)}
.brand{position:absolute;left:147px;top:22px;font-size:34px;font-weight:600;color:var(--brand-blue);letter-spacing:-0.5px}
.main-nav a{position:absolute;top:31px;font-size:17px;color:#555;text-decoration:none}
.main-nav a.active{color:var(--green)}
.main-nav a.active::after{content:"";position:absolute;left:-4px;right:-4px;top:54px;height:3px;background:var(--green)}

/* hero */
.hero{position:absolute;top:90px;left:0;width:1200px;height:555px;
  background:radial-gradient(ellipse at 60% 40%,#4f8ea0 0%,#2a5d72 40%,#17364a 100%)}
.hero-title{position:absolute;left:134px;top:210px;font-size:41px;line-height:51px;font-weight:600;color:var(--white);letter-spacing:0.5px}
.slider-dots{position:absolute;left:556px;top:514px;display:flex;gap:9px}
.slider-dots span{width:14px;height:14px;border-radius:50%;border:2px solid var(--white);background:var(--white)}
.slider-dots span:first-child{background:transparent}

/* what we do */
.section-title{font-size:30px;font-weight:600;color:#3b3b3b}
.about-title{left:145px;top:720px}
.about-text{left:147px;top:774px;width:520px;font-size:13.5px;line-height:23px;color:#555}
.about-text p+p{margin-top:14px}
.btn-primary{position:absolute;left:147px;top:949px;width:247px;height:44px;background:var(--navy);color:var(--white);font-size:15px;font-weight:600;display:flex;align-items:center;justify-content:center;gap:6px;border-radius:2px}

.contact-card{position:absolute;left:733px;top:698px;width:308px;height:314px;border:1px solid #ddd;background:var(--white)}
.contact-card h3{height:48px;background:#f1f1f1;font-size:21px;font-weight:400;color:var(--green);padding:11px 0 0 32px}
.field{position:absolute;left:31px;width:253px;height:35px;border:1px solid var(--line);font-size:12px;color:#888;padding:10px 0 0 14px}
.btn-submit{position:absolute;left:31px;top:250px;width:253px;height:38px;background:var(--green);color:var(--white);font-size:16px;font-weight:700;display:flex;align-items:center;justify-content:center}

/* book */
.book-band{position:absolute;top:1092px;left:0;width:1200px;height:442px;
  background:linear-gradient(100deg,#6b8a5d 0%,#4a7272 35%,#2a5689 65%,#1a4686 100%)}
.book-cover{position:absolute;left:212px;top:65px;width:218px;height:310px;
  background:linear-gradient(90deg,#142a55 0%,#1b2f5a 88%,#cfd3dc 90%,#eef0f4 100%);box-shadow:4px 6px 10px rgba(0,0,0,.35)}
.book-title{left:548px;top:76px;color:var(--white);font-size:30px;font-weight:600}
.book-text{left:548px;top:126px;width:480px;font-size:13.5px;line-height:23px;color:#e6ecf3}
.book-text p+p{margin-top:14px}
.btn-ghost{position:absolute;left:551px;top:325px;width:115px;height:34px;border:1.5px solid var(--white);color:var(--white);font-size:12px;display:flex;align-items:center;justify-content:center}

/* services */
.services{position:absolute;top:1534px;left:0;width:1200px;height:457px;
  background:radial-gradient(ellipse at 50% 50%,#ffffff 55%,#eaf1f8 100%)}
.services-title{position:absolute;top:38px;width:1200px;text-align:center;font-size:30px;font-weight:700;color:var(--navy)}
.service-card{position:absolute;top:100px;width:292px;height:304px;background:var(--white);border:2px solid #d8dbe0;text-align:center}
.service-card svg{position:absolute;left:111px;top:20px}
.service-card h4{position:absolute;top:107px;width:100%;font-size:20px;line-height:25px;font-weight:400;color:#333}
.service-card p{position:absolute;top:170px;left:30px;right:30px;font-size:11.5px;line-height:19px;color:#666}
.btn-outline{position:absolute;left:88px;top:246px;width:115px;height:34px;border:1.5px solid var(--navy);color:var(--navy);font-size:12px;display:flex;align-items:center;justify-content:center}

/* newsletter */
.news-title{position:absolute;top:2055px;width:1200px;text-align:center;font-size:25px;font-weight:600;color:#3b3b3b}
.news-text{position:absolute;top:2100px;left:320px;width:560px;text-align:center;font-size:13px;line-height:24px;color:#999}
.news-input{position:absolute;left:300px;top:2165px;width:458px;height:44px;border:1px solid var(--line);display:flex;align-items:center;gap:10px;padding-left:14px;font-size:15px;color:#999}
.news-btn{position:absolute;left:758px;top:2165px;width:138px;height:44px;background:var(--navy);color:var(--white);font-size:18px;font-weight:600;display:flex;align-items:center;justify-content:center}

/* footer */
.site-footer{position:absolute;top:2297px;left:0;width:1200px;height:354px;background:var(--footer-green);color:#eaf4dc}
.footer-brand{position:absolute;left:150px;top:82px;font-size:39px;font-weight:400;color:#c9e0ad;letter-spacing:-0.5px}
.footer-col h5{font-size:21px;font-weight:400;color:var(--white);margin-bottom:10px}
.footer-col{position:absolute;top:58px;font-size:13.5px;line-height:26px}
.contact-line{display:flex;gap:10px;align-items:flex-start}
.contact-line svg{flex:none;margin-top:5px}
.social{display:flex;gap:12px;margin-top:2px}
.social span{width:33px;height:33px;border-radius:50%;background:#f2f2f2}
.footer-rule{position:absolute;left:150px;top:274px;width:900px;height:1px;background:rgba(255,255,255,.25)}
.copyright{position:absolute;top:305px;width:1200px;text-align:center;font-size:12px;color:#dcebc6}
</style>
</head>
<body>

<header class="site-header">
  <div class="brand">Lumora Partners</div>
  <nav class="main-nav">
    <a class="active" style="left:544px">Home</a>
    <a style="left:640px">Book</a>
    <a style="left:726px">Services</a>
    <a style="left:839px">Downloadable Research</a>
  </nav>
</header>

<section class="hero">
  <div class="abs" role="img" aria-label="Photo of hands touching a transparent digital tablet with glowing transformation interface" style="inset:0"></div>
  <h1 class="hero-title">DIGITAL TRANSFORMATION<br>CONSULTING SERVICES</h1>
  <div class="slider-dots"><span></span><span></span><span></span><span></span></div>
</section>

<h2 class="abs section-title about-title">WHAT WE DO</h2>
<div class="abs about-text">
  <p>Meridian Capital Holdings is a private Qatari company that aims to provide secure and technologically advanced methods of trading to its clients. Those facilities enables clients to trade faster, more secure &amp; private. Having this strategy in our in minds, with this online portal we begin.</p>
  <p>Praesent elementum elit at tellus nec ultricies sit amet porttitor mattis enim In massa libero interdum nec interdum vel blandit sed nulla In</p>
</div>
<div class="btn-primary">Download Research Reports
  <svg width="12" height="12" viewBox="0 0 12 12"><path d="M1 6h9M6 2l4 4-4 4" stroke="#fff" stroke-width="2" fill="none"/></svg>
</div>

<form class="contact-card">
  <h3>Contact Form</h3>
  <div class="field" style="top:75px">First Name</div>
  <div class="field" style="top:117px">Last Name</div>
  <div class="field" style="top:160px">Email address</div>
  <div class="field" style="top:202px">Phone</div>
  <div class="btn-submit">SUBMIT</div>
</form>

<section class="book-band">
  <div class="book-cover" role="img" aria-label="Cover of the book Building Digital Well by Adrian Vell"></div>
  <h2 class="abs book-title">OUR BOOK</h2>
  <div class="abs book-text">
    <p>Building Digital Well is a manual for winning in the next digital era. Its author, Adrian Vell, has been helping large companies establish and execute digital strategies for 25 years.</p>
    <p>It is critical for any executive in any function to understand key digital technologies, the way they are evolving, how companies can leverage them to improve products, processes, and the customer journey, and what kind of business outcomes can be derived</p>
  </div>
  <div class="btn-ghost">READ MORE</div>
</section>

<section class="services">
  <div class="abs" role="img" aria-label="Soft background of connected network lines and nodes" style="inset:0"></div>
  <h2 class="services-title">OUR SERVICES</h2>

  <div class="service-card" style="left:150px">
    <svg width="70" height="70" viewBox="0 0 70 70" fill="none" stroke="#2a5ea8" stroke-width="3" stroke-linejoin="round">
      <path d="M6 28h12l30-16v42L18 40H6z"/><path d="M14 40l6 20h8l-4-18"/>
      <path d="M55 22q6 11 0 22M61 16q10 17 0 34"/>
    </svg>
    <h4>Speaking<br>Engagements</h4>
    <p>Provide an overview of the state of digital technology and implications for products, processes and customer journeya</p>
    <div class="btn-outline">READ MORE</div>
  </div>

  <div class="service-card" style="left:454px">
    <svg width="70" height="70" viewBox="0 0 70 70" fill="none" stroke="#2a5ea8" stroke-width="3">
      <circle cx="35" cy="35" r="8"/><circle cx="10" cy="12" r="5"/><circle cx="60" cy="10" r="5"/>
      <circle cx="10" cy="60" r="5"/><circle cx="60" cy="58" r="5"/>
      <path d="M14 16l15 13M56 14L41 29M14 56l15-15M56 54L41 41"/>
    </svg>
    <h4>Digital<br>Assessment</h4>
    <p>Provide an overview of the state of digital technology and implications for products, processes and customer journeya</p>
    <div class="btn-outline">READ MORE</div>
  </div>

  <div class="service-card" style="left:758px">
    <svg width="70" height="70" viewBox="0 0 70 70" fill="#2a6cc0">
      <circle cx="24" cy="22" r="16"/><circle cx="24" cy="22" r="6" fill="#fff"/>
      <circle cx="48" cy="48" r="13"/><circle cx="48" cy="48" r="5" fill="#fff"/>
      <circle cx="16" cy="52" r="9"/><circle cx="16" cy="52" r="3.5" fill="#fff"/>
    </svg>
    <h4>Digital Strategy<br>Development</h4>
    <p>Provide an overview of the state of digital technology and implications for products, processes and customer journeya</p>
    <div class="btn-outline">READ MORE</div>
  </div>
</section>

<h2 class="news-title">JOIN OUR NEWSLETTERS</h2>
<p class="news-text">Maecenas aliquet velit vel turpis Mauris neque metus malesuada nec ultricies sit amet porttitor mattis enim In massa libero interdum nec interdum vel</p>
<div class="news-input">
  <svg width="20" height="15" viewBox="0 0 20 15"><rect width="20" height="15" rx="1" fill="#aaa"/><path d="M1 1l9 7 9-7" stroke="#fff" stroke-width="1.5" fill="none"/></svg>
  Email address
</div>
<div class="news-btn">Subscribe</div>

<footer class="site-footer">
  <div class="footer-brand">Lumora Partners</div>
  <div class="footer-col" style="left:436px">
    <h5>Company</h5>
    <div>About Us</div><div>Our Book</div><div>Services</div><div>Download Research</div>
  </div>
  <div class="footer-col" style="left:622px">
    <h5>Contact Us</h5>
    <div class="contact-line">
      <svg width="13" height="16" viewBox="0 0 13 16"><path d="M6.5 0A6.5 6.5 0 0 0 0 6.5C0 11 6.5 16 6.5 16S13 11 13 6.5A6.5 6.5 0 0 0 6.5 0z" fill="#fff"/><circle cx="6.5" cy="6.5" r="2.5" fill="#5a9e1a"/></svg>
      <div>120 Harbor Point Road Suite 4B<br>Eastfield, PA 19000</div>
    </div>
    <div class="contact-line">
      <svg width="14" height="14" viewBox="0 0 14 14"><path d="M3 0l3 3-2 2q2 4 5 5l2-2 3 3-2 3Q4 13 0 3z" fill="#fff"/></svg>
      <div>(555) 014-2200</div>
    </div>
    <div class="contact-line">
      <svg width="14" height="11" viewBox="0 0 14 11"><rect width="14" height="11" rx="1" fill="#fff"/><path d="M1 1l6 5 6-5" stroke="#5a9e1a" stroke-width="1.3" fill="none"/></svg>
      <div>info@lumorapartners-example.com</div>
    </div>
  </div>
  <div class="footer-col" style="left:892px">
    <h5>Follow Us</h5>
    <div class="social"><span></span><span></span><span></span><span></span></div>
  </div>
  <div class="footer-rule"></div>
  <div class="copyright">© 2017 Company Name&nbsp; All right reserved</div>
</footer>

</body>
</html>
```